Design gusset bag packaging for a high protein cake mix

We need packaging designed for a 4x6x2 3/8 silver metallic bag. It will hold high protein cake mix. I will attach current label designs that we have on the back. I want it to be catchy-- template will be posted as well. Please stick to 6 printing colors or less.

Target Market(s)

Fitness, diet, dessert

Font styles to use
Serif
Decorative
Script

Colors
86cfc6
87d0c7
33b8a4
f0494f
fbf289
f59195
85cae6

Requirements
Must have
• It must include the nutrition label. I will attach our current label. Must have our logo. Please change the title to Tiny Oak Bakery Cake Mix (it's in red on the label) and change applesauce serving to 1/2 cup from "1 serving". Please stick to 6 printing colors or less.
Nice to have
• Would love to top flap above the zipper to say Eat Cake, Get Oaky! And on the back top flap say "Sprinkles- Enjoy the little things in life" Would love to have some sprinkles scattered around the front of the package..maybe even to look like it's coming out of a sprinkle shaker. Please feel free to use a more modern looking font

```html
<!DOCTYPE html>
<html lang="en">
<head>
<meta charset="utf-8">
<title>Tiny Oak Bakery Cake Mix</title>
<link rel="stylesheet" href="https://fonts.googleapis.com/css2?family=Sue+Ellen+Francisco&family=Quicksand:wght@500;700&family=Montserrat:wght@700&display=swap">
<style>
  :root {
    --teal-deep: #2a9aa8;
    --teal-mid: #33b8a4;
    --aqua: #86cfc6;
    --sky: #85cae6;
    --coral: #f0494f;
    --pink: #f59195;
    --lemon: #fbf289;
    --ink-teal: #1f7a78;
    --ink-dark: #3d3d3d;
    --white: #ffffff;
  }
  * { margin: 0; padding: 0; box-sizing: border-box; }
  html, body { width: 800px; height: 1200px; overflow: hidden; background: var(--white); }
  .package {
    position: relative;
    width: 800px;
    height: 1200px;
    overflow: hidden;
    background: linear-gradient(135deg, #f6b6a0 0%, #cfeff0 22%, #b9e6e6 45%, #d9d6f0 70%, #c8ddf2 100%);
  }
  .top-flap {
    position: absolute; left: 0; top: 0; width: 800px; height: 288px;
    background: linear-gradient(150deg, #2fa082 0%, #2f9fb0 45%, #3aa7c2 75%, #2b9bae 100%);
    display: flex; align-items: center; justify-content: center;
  }
  .tagline {
    font-family: "Sue Ellen Francisco", cursive;
    font-size: 86px;
    color: var(--white);
    font-weight: 400;
    letter-spacing: 1px;
    margin-top: 6px;
  }
  .title-block {
    position: absolute; left: 0; top: 355px; width: 800px; text-align: center;
  }
  .brand-line {
    font-family: "Quicksand", sans-serif;
    font-weight: 500;
    font-size: 54px;
    color: var(--ink-teal);
    letter-spacing: 1px;
    line-height: 1;
  }
  .product-line {
    font-family: "Montserrat", sans-serif;
    font-weight: 700;
    font-size: 88px;
    color: var(--coral);
    letter-spacing: 3px;
    line-height: 1;
    margin-top: 14px;
  }
  .sprinkle-spill {
    position: absolute; left: 0; top: 800px; width: 800px; height: 340px;
    background: linear-gradient(180deg, rgba(245,145,149,0) 0%, rgba(245,145,149,0.45) 35%, rgba(133,202,230,0.55) 70%, rgba(251,242,137,0.55) 100%);
  }
  .label-oval {
    position: absolute; left: 144px; top: 560px; width: 512px; height: 344px;
  }
  .label-name {
    position: absolute; left: 144px; top: 650px; width: 512px; text-align: center;
    font-family: "Quicksand", sans-serif;
    font-weight: 700;
    font-size: 58px;
    line-height: 1.05;
    color: var(--ink-dark);
    text-transform: uppercase;
  }
  .label-web {
    position: absolute; left: 144px; top: 828px; width: 512px; text-align: center;
    font-family: "Quicksand", sans-serif;
    font-weight: 700;
    font-size: 20px;
    color: var(--ink-dark);
  }
  .bottom-band {
    position: absolute; left: 0; top: 1140px; width: 800px; height: 60px;
    background: var(--teal-deep);
  }
</style>
</head>
<body>
  <main class="package">
    <header class="top-flap">
      <p class="tagline">Eat Cake, Get Oaky!</p>
    </header>

    <section class="title-block">
      <h1>
        <span class="brand-line">Tiny Oak Bakery</span><br>
        <span class="product-line">CAKE MIX</span>
      </h1>
    </section>

    <div class="sprinkle-spill" role="img" aria-label="Photograph of colourful rainbow sprinkles scattered across the lower part of the bag"></div>

    <svg class="label-oval" viewBox="0 0 512 344" aria-hidden="true">
      <ellipse cx="256" cy="174" rx="252" ry="168" fill="#9a8fd0" opacity="0.25"/>
      <ellipse cx="256" cy="172" rx="246" ry="162" fill="var(--white)" stroke="var(--aqua)" stroke-width="8"/>
    </svg>
    <p class="label-name">Tiny Oak<br>Bakery</p>
    <p class="label-web">www.tinyoakbakery.com</p>

    <footer class="bottom-band"></footer>
  </main>
</body>
</html>
```